Business card design needed for a security services business.

We provide a wide range of security services from guard personnel to electronic systems.

Industry/Entity Type

Security Industry

Contact Information for Business Card

Brent Holloway, Owner Office: 780.555.0148; Cell: 780.555.0193 Email: brent@korvanshieldgroup.example; Address 20417 163 St Edmonton, AB T5X 2K8

Colors
0054AA
0677BA
7BADD7
CADEEF
E8F1F8

Requirements
Nice to have
• On the back of the card I would like to possible list the services I provide: Guards Mobiles Live Video Surveillance Access Intrusion

```html
<!DOCTYPE html>
<html lang="en">
<head>
<meta charset="utf-8">
<title>Korvan Shield Group – Business Card</title>
<link href="https://fonts.googleapis.com/css2?family=Lato:wght@400;700;900&display=swap" rel="stylesheet">
<style>
  :root {
    --brand-blue: #1656a8;
    --brand-grey: #6b6b6b;
    --ink: #2a2a2a;
    --paper: #ffffff;
    --card-black: #1c1c1d;
    --emboss: #2c2c2e;
    --stage: #e9ecef;
    --edge-blue: #1f5fbf;
  }
  * { box-sizing: border-box; margin: 0; padding: 0; }
  html, body { width: 1200px; height: 900px; overflow: hidden; }
  body {
    background: var(--stage);
    font-family: "Lato", sans-serif;
    display: flex;
    align-items: center;
    justify-content: center;
    gap: 30px;
  }
  .card {
    position: relative;
    width: 560px;
    height: 320px;
    border-radius: 18px;
    overflow: hidden;
    box-shadow: 0 6px 18px rgba(0,0,0,.18);
  }
  /* Front */
  .card--front { background: var(--paper); }
  .front__swoosh { position: absolute; inset: 0; width: 100%; height: 100%; }
  .front__brand {
    position: absolute;
    left: 34px;
    top: 118px;
    width: 230px;
    display: flex;
    align-items: center;
    gap: 10px;
  }
  .brand__square { width: 22px; height: 22px; background: var(--brand-blue); flex: none; }
  .brand__name {
    font-weight: 900;
    font-size: 24px;
    line-height: 1.05;
    color: var(--brand-blue);
    text-transform: uppercase;
    letter-spacing: .5px;
  }
  .front__divider {
    position: absolute;
    left: 280px;
    top: 42px;
    width: 2px;
    height: 150px;
    background: var(--brand-blue);
  }
  .front__details {
    position: absolute;
    left: 298px;
    top: 36px;
    color: var(--ink);
    font-size: 12.5px;
    line-height: 1.4;
  }
  .details__name { color: var(--brand-blue); font-weight: 700; font-size: 20px; line-height: 1.1; }
  .details__role { font-size: 12.5px; margin-bottom: 12px; }
  .details__address { margin-bottom: 10px; }
  .contact { display: flex; align-items: center; gap: 7px; }
  .contact svg { width: 12px; height: 12px; fill: var(--brand-blue); flex: none; }

  /* Back */
  .card--back {
    background: var(--card-black);
    border: 3px solid var(--edge-blue);
    color: #fff;
  }
  .back__brand {
    position: absolute;
    left: 0; right: 0;
    top: 78px;
    display: flex;
    align-items: center;
    justify-content: center;
    gap: 14px;
  }
  .back__brand .brand__square { width: 30px; height: 30px; background: var(--emboss); }
  .back__brand .brand__name { color: var(--emboss); font-size: 38px; }
  .back__rule {
    position: absolute;
    left: 120px; right: 80px;
    top: 150px;
    height: 2px;
    background: var(--emboss);
  }
  .back__tagline {
    position: absolute;
    left: 0; right: 0;
    top: 200px;
    text-align: center;
    font-weight: 700;
    font-size: 19px;
  }
  .back__services {
    position: absolute;
    left: 0; right: 0;
    top: 238px;
    text-align: center;
    font-size: 12px;
    letter-spacing: .2px;
  }
</style>
</head>
<body>

  <section class="card card--front" aria-label="Business card front">
    <svg class="front__swoosh" viewBox="0 0 560 320" preserveAspectRatio="none" aria-hidden="true">
      <path d="M200 320 C 340 270, 450 235, 560 205 L560 320 Z" fill="var(--brand-blue)"/>
      <path d="M240 320 C 360 280, 460 248, 560 222 L560 320 Z" fill="#ffffff"/>
      <path d="M252 320 C 370 285, 465 255, 560 230 L560 320 Z" fill="var(--brand-grey)"/>
    </svg>

    <div class="front__brand">
      <span class="brand__square"></span>
      <span class="brand__name">Korvan Shield Group</span>
    </div>

    <div class="front__divider"></div>

    <div class="front__details">
      <p class="details__name">Brent Holloway</p>
      <p class="details__role">Owner</p>
      <p class="details__address">20417 163 St Edmonton,<br>AB T5X 2K8</p>
      <p class="contact">
        <svg viewBox="0 0 24 24"><path d="M6.6 10.8a15 15 0 0 0 6.6 6.6l2.2-2.2c.3-.3.7-.4 1-.2 1.1.4 2.300.6 3.6.6.6 0 1 .4 1 1V20c0 .6-.4 1-1 1A17 17 0 0 1 3 4c0-.6.4-1 1-1h3.5c.6 0 1 .4 1 1 0 1.3.2 2.5.6 3.6.1.3 0 .7-.2 1z"/></svg>
        780.555.0148
      </p>
      <p class="contact">
        <svg viewBox="0 0 24 24"><path d="M7 1h10a2 2 0 0 1 2 2v18a2 2 0 0 1-2 2H7a2 2 0 0 1-2-2V3a2 2 0 0 1 2-2zm0 3v14h10V4zm5 15.5a1 1 0 1 0 0 2 1 1 0 0 0 0-2z"/></svg>
        780.555.0193
      </p>
      <p class="contact">
        <svg viewBox="0 0 24 24"><path d="M2 5h20v14H2zm2 2v.5l8 5 8-5V7zm0 2.8V17h16V9.8l-8 5z"/></svg>
        brent@korvanshieldgroup.example
      </p>
    </div>
  </section>

  <section class="card card--back" aria-label="Business card back">
    <div class="back__brand">
      <span class="brand__square"></span>
      <span class="brand__name">Korvan Shield Group</span>
    </div>
    <div class="back__rule"></div>
    <p class="back__tagline">services | provide</p>
    <p class="back__services">Guards Mobiles Live Video Surveillance Access Intrusion</p>
  </section>

</body>
</html>
```